Company website for an international IT business

We require a website for our business, Corvell Solutions. The business has two primary areas: Horizons, which includes two machine learning/deep learning based products and IT consultancy, which is the service we provide to other businesses.

We bridge cutting-edge research to market.

STYLING:
The site can be on single page or multi-page. This is fully open to suggestion. So long as the look and feel are consistent. Currently, we have no strong preference for colors, styles or layouts.
You can find the logo of our website in the attachment “Corvell-logo.png” and “Corvell-logo-landscape.png”.

CONTENT:
You can find the text of the website in “Website-Content.pdf”, which explains the services and products of our business. The format of the text is also open to suggestion - including breaking up the text into visually appealing sections.
We would also like to include suitable images on the website so that it does not appear to be a text-heavy page. We are happy to have placeholder images on stock image sites if needed. We are open to suggestions on placing of images

ATTACHMENT:

Industry/Entity Type

It Company

Coding

Coded - Design and coding required

Number of Pages Required

1 page

Colors

Designer to choose colors to be used in the design.

Requirements
Must have
• A full description of the requirement is in the attachment "Website-Content.pdf"
• The design must have HTML/CSS, and all resources relevant (images, fonts etc)
• We are
Nice to have
• We are open to suggestions on top of the requirement, please reach out and communicate.

```html
<!DOCTYPE html>
<html lang="en">
<head>
<meta charset="utf-8">
<title>Corvell Solutions</title>
<link href="https://fonts.googleapis.com/css2?family=Montserrat:wght@500;600;700&family=Open+Sans:ital,wght@0,400;0,600;1,400&display=swap" rel="stylesheet">
<style>
:root{
  --blue:#1a85c6;
  --blue-dark:#0d5f97;
  --blue-deep:#0b3d63;
  --ink:#111;
  --text:#444;
  --white:#fff;
  --black:#0a0a0a;
  --footer:#121a22;
}
*{margin:0;padding:0;box-sizing:border-box}
html,body{width:1200px;height:4110px;overflow:hidden}
body{position:relative;background:var(--white);font-family:"Open Sans",sans-serif;color:var(--text)}
.abs{position:absolute}
h1,h2,h3{font-family:"Montserrat",sans-serif}

/* header */
.topbar .social{position:absolute;top:6px;width:30px;height:30px;border:2px solid var(--blue);border-radius:50%}
.contact-top{position:absolute;top:8px;right:70px;font-size:17px;color:var(--blue);display:flex;gap:40px}
.contact-top span{display:flex;align-items:center;gap:8px}
.nav{position:absolute;top:80px;font-family:"Montserrat",sans-serif;font-size:15px;font-weight:500;color:#222;letter-spacing:.5px}
.nav.active{color:var(--blue)}
.brand-mark{position:absolute;left:560px;top:12px;width:80px;height:80px;border-radius:50%;background:var(--blue)}
.brand-name{position:absolute;left:500px;width:200px;top:98px;text-align:center;font-family:"Montserrat",sans-serif;font-weight:700;font-size:22px;color:var(--ink);letter-spacing:2px}

/* hero */
.hero{left:0;top:137px;width:1200px;height:500px}
.hero-title{left:580px;top:262px;font-weight:600;font-size:64px;color:var(--white);line-height:1.2}
.hero-sub{left:582px;top:344px;font-size:26px;font-weight:400;color:var(--white)}
.hero-text{left:582px;top:386px;width:560px;font-size:16px;font-style:italic;color:var(--white);line-height:1.45}
.btn{position:absolute;display:flex;align-items:center;justify-content:center;background:var(--blue);color:var(--white);font-family:"Montserrat",sans-serif;font-weight:600;border-radius:30px}
.service{position:absolute;width:240px;text-align:center;font-size:17px;color:#333;line-height:1.35}
.service-icon{position:absolute;width:128px;height:128px;border-radius:50%;background:var(--white);border:6px solid var(--blue);display:flex;align-items:center;justify-content:center}

/* welcome */
.section-title{position:absolute;left:0;width:1200px;text-align:center;font-weight:600;font-size:40px;color:var(--ink)}
.welcome-text{left:200px;top:940px;width:800px;text-align:center;font-size:14px;line-height:1.8;color:#333}

/* horizons */
.horizons{left:0;top:1090px;width:1200px;height:760px}
.product-title{left:77px;top:1322px;font-weight:600;font-size:40px;color:var(--white)}
.product-text{left:77px;top:1384px;width:585px;font-size:14px;line-height:1.65;color:var(--white)}
.product-text p{margin-bottom:12px}
.tabs{left:0;top:1781px;width:1200px;height:60px;background:var(--black)}
.tab{position:absolute;top:16px;font-family:"Montserrat",sans-serif;font-weight:600;font-size:22px;color:var(--white)}

/* process */
.process{left:0;top:1841px;width:1200px;height:480px}
.step-icon{position:absolute;width:124px;height:124px;border-radius:50%;background:var(--blue);display:flex;align-items:center;justify-content:center}
.step-label{position:absolute;width:300px;text-align:center;font-family:"Montserrat",sans-serif;font-weight:600;font-size:22px;color:var(--blue)}
.step-text{position:absolute;width:330px;text-align:center;font-size:15px;line-height:1.6;color:#333}

/* help */
.help-item{position:absolute;left:510px;display:flex;align-items:center;gap:30px;color:var(--white);font-size:16px;line-height:1.5}
.help-icon{flex:none;width:100px;height:100px;border-radius:50%;border:3px solid var(--white);display:flex;align-items:center;justify-content:center}

/* portfolio */
.tile{position:absolute;height:208px}
.tagline{left:0;width:1200px;top:2988px;text-align:center;font-size:16px;font-style:italic;color:#555}

/* footer */
.footer{left:0;top:3620px;width:1200px;height:430px}
.foot-title{position:absolute;top:3796px;font-weight:700;font-size:19px;color:var(--white)}
.foot-text{position:absolute;font-size:14px;line-height:1.75;color:#d6dde3}
.foot-contact{position:absolute;left:370px;display:flex;align-items:center;gap:16px;font-size:14px;color:#d6dde3;line-height:1.6}
.foot-contact i{flex:none;width:38px;height:38px;border-radius:50%;background:var(--blue);display:flex;align-items:center;justify-content:center}
.copyright{left:0;top:4047px;width:1200px;height:63px;background:var(--blue);color:var(--white);font-size:14px;text-align:center;line-height:63px}
</style>
</head>
<body>

<!-- header -->
<header class="topbar">
  <span class="social" style="left:76px"></span>
  <span class="social" style="left:114px"></span>
  <span class="social" style="left:152px"></span>
  <div class="contact-top">
    <span><svg width="20" height="14" viewBox="0 0 20 14"><rect x="1" y="1" width="18" height="12" fill="none" stroke="#1a85c6" stroke-width="2"/><path d="M1 1l9 7 9-7" fill="none" stroke="#1a85c6" stroke-width="2"/></svg>info@corvell-solutions.com</span>
    <span><svg width="16" height="16" viewBox="0 0 16 16"><path d="M3 1l3 3-2 2a9 9 0 006 6l2-2 3 3-2 2C7 15 1 9 1 3z" fill="#1a85c6"/></svg>555 014 2290</span>
  </div>
  <span class="nav active" style="left:224px">HOME</span>
  <span class="nav" style="left:318px">ABOUT US</span>
  <span class="nav" style="left:425px">HORIZONS</span>
  <span class="brand-mark"></span>
  <span class="brand-name">CORVELL</span>
  <span class="nav" style="left:712px">IT CONSULTANCY</span>
  <span class="nav" style="left:877px">CONTACT US</span>
  <svg class="abs" style="left:997px;top:79px" width="20" height="20" viewBox="0 0 20 20"><circle cx="8" cy="8" r="6" fill="none" stroke="#1a85c6" stroke-width="2.5"/><path d="M12.5 12.5L18 18" stroke="#1a85c6" stroke-width="2.5"/></svg>
</header>

<!-- hero -->
<svg class="abs hero" viewBox="0 0 1200 500" role="img" aria-label="Photo of two business people reviewing a phone in a bright office">
  <defs>
    <linearGradient id="heroBg" x1="0" y1="0" x2="1" y2=".3">
      <stop offset="0" stop-color="#dfe3e6"/>
      <stop offset=".22" stop-color="#b9c1c7"/>
      <stop offset=".42" stop-color="#8d979f"/>
      <stop offset=".62" stop-color="#5f6c76"/>
      <stop offset="1" stop-color="#33434f"/>
    </linearGradient>
    <radialGradient id="heroGlow" cx=".28" cy=".45" r=".35">
      <stop offset="0" stop-color="#e9dccf" stop-opacity=".55"/>
      <stop offset="1" stop-color="#e9dccf" stop-opacity="0"/>
    </radialGradient>
  </defs>
  <path d="M0 0H1200V460Q600 360 0 460Z" fill="url(#heroBg)"/>
  <path d="M0 0H1200V460Q600 360 0 460Z" fill="url(#heroGlow)"/>
  <path d="M0 440Q600 330 1200 440V470Q600 350 0 470Z" fill="#1a85c6"/>
  <path d="M44 228l-12 14 12 14M1156 228l12 14-12 14" fill="none" stroke="#fff" stroke-width="3"/>
</svg>
<div class="abs hero-title">Corvell Solutions</div>
<div class="abs hero-sub">We Solve "HARD" Problems For Business</div>
<div class="abs hero-text">We have many years experience in machine learning, data mining, app development, DevOps and hardware design</div>
<a class="btn" style="left:580px;top:455px;width:196px;height:50px;font-size:19px">CONTACT US</a>

<div class="service-icon" style="left:198px;top:600px"><svg width="60" height="50" viewBox="0 0 60 50"><rect x="4" y="4" width="52" height="34" rx="3" fill="none" stroke="#1a85c6" stroke-width="3"/><path d="M20 46h20M30 38v8M14 16h16M14 24h26" stroke="#1a85c6" stroke-width="3"/></svg></div>
<div class="service" style="left:144px;top:744px">Software<br>Development</div>
<div class="service-icon" style="left:533px;top:628px"><svg width="56" height="56" viewBox="0 0 56 56"><circle cx="28" cy="28" r="22" fill="none" stroke="#1a85c6" stroke-width="3"/><path d="M6 28h44M28 6c-10 12-10 32 0 44M28 6c10 12 10 32 0 44" fill="none" stroke="#1a85c6" stroke-width="3"/></svg></div>
<div class="service" style="left:478px;top:772px">IOT System<br>Design</div>
<div class="service-icon" style="left:854px;top:608px"><svg width="48" height="56" viewBox="0 0 48 56"><rect x="4" y="4" width="40" height="48" rx="4" fill="none" stroke="#1a85c6" stroke-width="3"/><path d="M12 16h24M12 26h24M12 36h14" stroke="#1a85c6" stroke-width="3"/></svg></div>
<div class="service" style="left:798px;top:756px">Machine learning<br>solutions</div>

<!-- welcome -->
<h2 class="section-title" style="top:878px">WELCOME TO CORVELL</h2>
<p class="abs welcome-text">Corvell Solutions is an IT consultancy firm with a difference We can provide IT expertise for your business at any stage - from initial idea to live systems. Corvell Solutions is an IT consultancy firm with a difference We can provide IT expertise for your business at any stage</p>
<svg class="abs" style="left:580px;top:1028px" width="40" height="16" viewBox="0 0 40 16"><path d="M2 8h34M28 2l8 6-8 6" fill="none" stroke="#1a85c6" stroke-width="3"/></svg>

<!-- horizons -->
<svg class="abs horizons" viewBox="0 0 1200 760" role="img" aria-label="Blue abstract background">
  <defs><linearGradient id="hzBg" x1="0" y1="0" x2="1" y2="1"><stop offset="0" stop-color="#2b93d1"/><stop offset="1" stop-color="#0f5e96"/></linearGradient></defs>
  <path d="M0 120Q600 -60 1200 120V760H0Z" fill="url(#hzBg)"/>
</svg>
<h2 class="section-title" style="top:1160px">OUR HORIZONS</h2>
<p class="abs" style="left:300px;top:1226px;width:600px;text-align:center;font-size:16px;line-height:1.6;color:var(--white)">Corvell horizons has developed two cutting edge products using machine learning and deep learning.</p>
<h3 class="abs product-title">SENTRA</h3>
<div class="abs product-text">
  <p>The primary cause of accidents on the road are caused by human error. Of these driver distraction and fatigue are the real problem.</p>
  <p>SENTRA is a system for HGV/HMT drivers to make every journey safer - safer for the driver and safer to other road users.</p>
  <p>SENTRA uses advanced deep learning techniques to monitor driver behavior in real time inside the cabin. SENTRA can detect driver distraction (mobile phone usage, smoking, failure to focused on the road ahead) and also monitor for classic signs of fatigue. Current ADAS systems focus on external factors such as speed, distance to the vehicle ahead, keeping within road markings.</p>
  <p>By monitoring drivers for potentially dangerous driving situations SENTRA can improve safety and lower insurance costs without the need for human monitoring. This allows road freight operations to be in compliance with upcoming government regulations.</p>
</div>
<div class="abs" role="img" aria-label="Illustration of a driver inside a car cabin being monitored by a scanning system" style="left:685px;top:1334px;width:515px;height:398px;background:radial-gradient(ellipse at 45% 55%,#c9d3da 0,#9aa8b3 35%,#56656f 75%,#2f3b44 100%)"></div>
<div class="abs tabs">
  <svg class="abs" style="left:236px;top:-20px" width="54" height="30" viewBox="0 0 54 30"><path d="M0 30A27 27 0 0154 30Z" fill="#0a0a0a"/><circle cx="27" cy="20" r="4" fill="#fff"/></svg>
  <span class="tab" style="left:222px">SENTRA</span>
  <span class="tab" style="left:845px">TREADCHECK</span>
</div>

<!-- process -->
<div class="abs process" role="img" aria-label="Faded photo of a team with connected profile portraits" style="background:radial-gradient(ellipse at 25% 40%,#f4f7f9 0,#e3eaef 45%,#cbd7e0 100%)"></div>
<h2 class="section-title" style="top:1900px">ITERATIVE AGILE PROCESS</h2>
<svg class="abs" style="left:300px;top:2020px" width="600" height="60" viewBox="0 0 600 60"><path d="M10 45Q120 -5 230 35M370 35Q480 -5 590 40" fill="none" stroke="#333" stroke-width="2" stroke-dasharray="8 7"/></svg>
<div class="step-icon" style="left:179px;top:2007px"><svg width="50" height="60" viewBox="0 0 50 60"><rect x="6" y="4" width="38" height="52" rx="3" fill="none" stroke="#fff" stroke-width="3"/><path d="M14 18h22M14 28h22M14 38h14" stroke="#fff" stroke-width="3"/></svg></div>
<div class="step-icon" style="left:535px;top:2007px"><svg width="56" height="56" viewBox="0 0 56 56"><path d="M6 6h18v8a5 5 0 0110 0V6h16v18h-8a5 5 0 000 10h8v16H6z" fill="none" stroke="#fff" stroke-width="3"/></svg></div>
<div class="step-icon" style="left:897px;top:2007px"><svg width="64" height="46" viewBox="0 0 64 46"><rect x="4" y="6" width="34" height="26" fill="none" stroke="#fff" stroke-width="3"/><path d="M38 14h12l10 10v8H38" fill="none" stroke="#fff" stroke-width="3"/><circle cx="16" cy="38" r="5" fill="none" stroke="#fff" stroke-width="3"/><circle cx="48" cy="38" r="5" fill="none" stroke="#fff" stroke-width="3"/></svg></div>
<div class="step-label" style="left:91px;top:2148px">DEFINE</div>
<div class="step-label" style="left:447px;top:2148px">BUILD</div>
<div class="step-label" style="left:809px;top:2148px">DELIVER</div>
<p class="step-text" style="left:76px;top:2184px">Our conversation will start with a high-level agreement on the overall strategy Our tech team will research &amp; investigate.</p>
<p class="step-text" style="left:432px;top:2184px">We follow a scrum methodology in our development process, that is, we carry out the work in multiple (bi-)weekly sprints.</p>
<p class="step-text" style="left:794px;top:2184px">At the end of a contract, we ship deliverables with sufficient documentations. In addition, we will provide free support.</p>

<!-- help -->
<svg class="abs" style="left:0;top:2315px" width="1200" height="560" viewBox="0 0 1200 560">
  <defs>
    <linearGradient id="helpBg" x1="0" x2="1"><stop offset="0" stop-color="#0f6aa8"/><stop offset="1" stop-color="#1d8bcc"/></linearGradient>
    <radialGradient id="helpPhoto" cx=".5" cy=".45" r=".6">
      <stop offset="0" stop-color="#b9c2c9"/>
      <stop offset=".5" stop-color="#7f95a6" stop-opacity=".75"/>
      <stop offset="1" stop-color="#1a77b6" stop-opacity="0"/>
    </radialGradient>
  </defs>
  <path d="M0 0H1200V440Q600 620 0 440Z" fill="url(#helpBg)"/>
  <rect x="70" y="20" width="430" height="520" fill="url(#helpPhoto)" role="img" aria-label="Photo of a smiling businessman in a grey shirt with arms crossed"/>
</svg>
<h2 class="section-title" style="left:300px;width:600px;top:2368px;font-size:36px">HOW CAN WE HELP</h2>
<div class="help-item" style="top:2452px"><span class="help-icon"><svg width="50" height="36" viewBox="0 0 64 46"><rect x="4" y="6" width="34" height="26" fill="none" stroke="#fff" stroke-width="3"/><path d="M38 14h12l10 10v8H38" fill="none" stroke="#fff" stroke-width="3"/><circle cx="16" cy="38" r="5" fill="none" stroke="#fff" stroke-width="3"/><circle cx="48" cy="38" r="5" fill="none" stroke="#fff" stroke-width="3"/></svg></span>Acquire more development capacity and get<br>Results fast.</div>
<div class="help-item" style="top:2575px;left:590px"><span class="help-icon"><svg width="40" height="50" viewBox="0 0 40 50"><path d="M12 4h16l-5 8h-6zM8 16h24q8 10 6 22-2 8-18 8T2 38q-2-12 6-22z" fill="none" stroke="#fff" stroke-width="3"/><path d="M20 20v20M25 25h-7a3 3 0 000 6h4a3 3 0 010 6h-7" fill="none" stroke="#fff" stroke-width="2.5"/></svg></span>Avoid the overhead incurred by frequent scaling<br>of your development team</div>
<div class="help-item" style="top:2698px"><span class="help-icon"><svg width="54" height="54" viewBox="0 0 56 56"><circle cx="28" cy="28" r="22" fill="none" stroke="#fff" stroke-width="3"/><path d="M6 28h44M28 6c-10 12-10 32 0 44M28 6c10 12 10 32 0 44" fill="none" stroke="#fff" stroke-width="3"/></svg></span>Reach a wide spectrum of expertise.</div>

<!-- portfolio -->
<h2 class="section-title" style="top:2928px">OUR PORTFOLIO</h2>
<p class="abs tagline">Lorem Ipsum is simply dummy text of the printing and typesetting industry.</p>
<div class="tile" role="img" aria-label="Portfolio project screenshot with magnifier overlay" style="left:77px;top:3041px;width:334px;background:radial-gradient(ellipse at 40% 50%,#5cc2cf 0,#2aa3b9 45%,#1a7fbd 100%)"></div>
<svg class="abs" style="left:214px;top:3112px" width="60" height="60" viewBox="0 0 60 60"><circle cx="30" cy="30" r="28" fill="#fff"/><circle cx="27" cy="27" r="10" fill="none" stroke="#1a85c6" stroke-width="4"/><path d="M34 34l9 9" stroke="#1a85c6" stroke-width="4"/></svg>
<div class="tile" role="img" aria-label="Cover of a book on deep learning for natural language processing" style="left:433px;top:3041px;width:334px;background:linear-gradient(120deg,#16284a 0,#1f3a66 55%,#3b6fa8 100%)"></div>
<div class="tile" role="img" aria-label="Cover of a book on applied machine learning and deep learning" style="left:789px;top:3041px;width:334px;background:linear-gradient(180deg,#e8862c 0 14%,#2f62c8 14%,#4a86e0 100%)"></div>
<div class="tile" role="img" aria-label="Promotional banner for a deep learning book" style="left:255px;top:3269px;width:334px;height:211px;background:linear-gradient(120deg,#8bc653 0,#a9d27a 60%,#c9a27f 100%)"></div>
<div class="tile" role="img" aria-label="Diagram of a cloud machine learning architecture" style="left:611px;top:3269px;width:334px;height:211px;background:linear-gradient(180deg,#2b73c2 0 14%,#eef4fa 14%,#d7e5f2 100%)"></div>
<a class="btn" style="left:501px;top:3502px;width:198px;height:52px;font-size:19px">VIEW MORE</a>

<!-- footer -->
<svg class="abs footer" viewBox="0 0 1200 430" role="img" aria-label="Dark background photo of people at a desk">
  <defs><linearGradient id="footBg" x1="0" y1="0" x2="1" y2="1"><stop offset="0" stop-color="#1c2630"/><stop offset="1" stop-color="#0e151c"/></linearGradient></defs>
  <path d="M0 40Q600 -30 1200 40V430H0Z" fill="url(#footBg)"/>
</svg>
<span class="abs" style="left:560px;top:3664px;width:80px;height:80px;border-radius:50%;background:var(--blue)"></span>
<span class="abs" style="left:500px;top:3752px;width:200px;text-align:center;font-family:Montserrat,sans-serif;font-weight:700;font-size:20px;letter-spacing:2px;color:#fff">CORVELL</span>
<h3 class="foot-title" style="left:82px">ABOUT US</h3>
<h3 class="foot-title" style="left:370px">CONTACT INFO</h3>
<h3 class="foot-title" style="left:652px">HORIZONS</h3>
<h3 class="foot-title" style="left:877px">NEWSLETTER</h3>
<p class="foot-text" style="left:82px;top:3840px;width:250px">We have many years experience in machine learning, data mining, app development, DevOps and hardware design. We solve "hard" problems for business.. <span style="color:var(--blue);text-decoration:underline">Read More</span></p>
<div class="foot-contact" style="top:3840px"><i><svg width="14" height="18" viewBox="0 0 14 18"><path d="M7 17S1 10 1 7a6 6 0 0112 0c0 3-6 10-6 10z" fill="#fff"/><circle cx="7" cy="7" r="2" fill="#1a85c6"/></svg></i><span>101 - Lorem Ipsum is the text<br>simple dummy text of print</span></div>
<div class="foot-contact" style="top:3898px"><i><svg width="16" height="16" viewBox="0 0 16 16"><path d="M3 1l3 3-2 2a9 9 0 006 6l2-2 3 3-2 2C7 15 1 9 1 3z" fill="#fff"/></svg></i><span>555 014 2290</span></div>
<div class="foot-contact" style="top:3956px"><i><svg width="18" height="13" viewBox="0 0 20 14"><rect x="1" y="1" width="18" height="12" fill="#fff"/><path d="M1 1l9 7 9-7" fill="none" stroke="#1a85c6" stroke-width="2"/></svg></i><span>info@corvell-solutions.com</span></div>
<p class="foot-text" style="left:652px;top:3838px">•&nbsp; Sentra<br>•&nbsp; Treadcheck</p>
<p class="foot-text" style="left:877px;top:3832px;width:260px">Would you like to receive exclusive access to articles, white papers and our regular monthly newsletter?</p>
<div class="abs" style="left:877px;top:3906px;width:246px;height:42px;background:#fff;font-size:13px;color:#555;padding:11px 10px">Enter Email Id *</div>
<a class="btn" style="left:877px;top:3958px;width:180px;height:46px;font-size:18px">SUBSCRIBE</a>
<div class="abs copyright">© CORVELL - 2018 All Right Reserved.</div>

</body>
</html>
```